Biz Card for Marla Dempsey Insurance Agency
Biz Card for Marla Dempsey Insurance Agency - Financial Services
Creative Brief
Bright & Fun-filled
Marla Dempsey
Independent Agent
Briarton, NC
office 336-521-0974
cell 336-597-2160
marladempsey34@qorvinmail.com
please include her picture in her new card. I will also upload a copy of what we are currently using. she needs something new and fresh. please use the new logo we upload.
Also, please see the words we are using for the back of her card, please use those same words on the new cards.

```html
<!DOCTYPE html>
<html lang="en">
<head>
<meta charset="utf-8">
<title>Marla Dempsey Insurance Agency – Business Card</title>
<link href="https://fonts.googleapis.com/css2?family=Cinzel:wght@400;600;700&display=swap" rel="stylesheet">
<style>
  :root {
    --bg: #2b2d31;
    --card: #ffffff;
    --card-shade: #eef0f3;
    --navy: #1d2f5e;
    --ink: #2a2a2a;
    --green: #2f8a2f;
    --photo-top: #8a5a44;
    --photo-bottom: #2e3b55;
  }
  * { margin: 0; padding: 0; box-sizing: border-box; }
  html, body { width: 1200px; height: 850px; overflow: hidden; }
  body {
    background: var(--bg);
    font-family: "Cinzel", serif;
    position: relative;
  }
  .card {
    position: absolute;
    width: 520px;
    height: 300px;
    border-radius: 22px;
    background: linear-gradient(180deg, var(--card) 70%, var(--card-shade) 100%);
    box-shadow: 0 10px 30px rgba(0,0,0,.45);
    overflow: hidden;
  }
  .card--front { left: 120px; top: 110px; }
  .card--back { left: 560px; top: 440px; }

  /* front */
  .agency-mark {
    position: absolute; left: 38px; top: 66px;
    display: flex; align-items: center; gap: 10px;
  }
  .agency-mark__dot { width: 34px; height: 34px; border-radius: 50%; background: var(--green); flex: none; }
  .agency-mark__name {
    color: var(--navy); font-weight: 600; font-size: 15px; line-height: 1.15;
    text-transform: uppercase; letter-spacing: .5px; width: 170px;
  }
  .portrait {
    position: absolute; left: 332px; top: 16px;
    width: 122px; height: 114px; border-radius: 12px;
    background: linear-gradient(180deg, var(--photo-top), var(--photo-bottom));
  }
  .agent {
    position: absolute; left: 293px; top: 146px; width: 200px; text-align: center;
    color: var(--navy);
  }
  .agent__name { font-size: 18px; font-weight: 400; }
  .agent__title { font-size: 15px; font-weight: 400; margin-top: 2px; }
  .contact {
    position: absolute; left: 34px; top: 176px;
    color: var(--ink); font-size: 13px; line-height: 21px; letter-spacing: .4px;
  }
  .contact dt { display: inline-block; width: 78px; text-transform: lowercase; }
  .contact dd { display: inline; }
  .contact__city { margin-bottom: 6px; }
  .email {
    position: absolute; left: 262px; top: 236px;
    color: var(--ink); font-size: 12.5px; letter-spacing: .3px;
  }

  /* back */
  .statement {
    position: absolute; left: 20px; top: 26px; width: 480px; text-align: center;
    color: var(--navy); font-weight: 700; font-size: 15px; line-height: 20px;
    text-transform: uppercase; letter-spacing: .5px;
  }
  .services {
    position: absolute; left: 58px; top: 118px; list-style: none;
    color: var(--ink); font-size: 13.5px; line-height: 21px; text-transform: uppercase;
  }
  .services li { display: flex; align-items: center; gap: 10px; }
  .services li::before {
    content: ""; width: 7px; height: 7px; border-radius: 50%; background: var(--navy); flex: none;
  }
</style>
</head>
<body>
  <section class="card card--front">
    <div class="agency-mark">
      <span class="agency-mark__dot"></span>
      <span class="agency-mark__name">Marla Dempsey Insurance Agency</span>
    </div>
    <div class="portrait" role="img" aria-label="Portrait photo of Marla Dempsey"></div>
    <div class="agent">
      <p class="agent__name">Marla Dempsey</p>
      <p class="agent__title">Independent Agent</p>
    </div>
    <dl class="contact">
      <div class="contact__city">Briarton, NC</div>
      <div><dt>toll free :</dt><dd>888-640-2715</dd></div>
      <div><dt>office :</dt><dd>336-521-0974</dd></div>
      <div><dt>cell :</dt><dd>336-597-2160</dd></div>
    </dl>
    <p class="email">marladempsey34@qorvinmail.com</p>
  </section>

  <section class="card card--back">
    <p class="statement">I represent companies that offer the products and services you may need inorder to be better prepared for the future .</p>
    <ul class="services">
      <li>Long-Term Care Insurance</li>
      <li>Fixed Annuities</li>
      <li>Life Insurance</li>
      <li>Medicare Supplement Insurance</li>
      <li>Individual Major Medical Insurance</li>
      <li>Final Expense Insurance</li>
      <li>Medicare Advantage Plans</li>
    </ul>
  </section>
</body>
</html>
```